Boutique sales recruiting firm needs dual purpose business card

We need a business card designed for a sales recruiting company called Brisk Otter Recruiting. We help both sales reps looking for work as well as companies looking for talent. What makes us unique is that 'we like to hunt', not literally but hunt for great companies and greats recruits. We are looking for a business card that on one side targets sales reps looking for work and on the other side companies looking for sales reps that incorporates the feel of a "Brisk Otter" as well as having dual personalities.

```html
<!DOCTYPE html>
<html lang="en">
<head>
<meta charset="utf-8">
<title>Brisk Otter Recruiting – Business Card</title>
<link href="https://fonts.googleapis.com/css2?family=Lexend:wght@300;400;600;700&display=swap" rel="stylesheet">
<style>
  :root {
    --ink: #0b0f10;
    --paper: #ffffff;
    --amber: #eba12a;
    --stage: #2a2b2d;
    --muted: #e8e8e8;
  }
  * { margin: 0; padding: 0; box-sizing: border-box; }
  html, body { width: 1200px; height: 1200px; overflow: hidden; }
  body {
    background: var(--stage);
    font-family: "Lexend", sans-serif;
    display: flex;
    flex-direction: column;
    align-items: center;
    justify-content: center;
    gap: 60px;
  }
  .card {
    position: relative;
    width: 900px;
    height: 514px;
    overflow: hidden;
  }
  /* Back side */
  .card--back {
    background: radial-gradient(circle at 45% 40%, #121819 0%, var(--ink) 70%);
    display: flex;
    align-items: center;
    justify-content: center;
  }
  .wordmark {
    font-weight: 600;
    letter-spacing: 0.01em;
    line-height: 1;
  }
  .card--back .wordmark { color: var(--paper); font-size: 64px; }
  /* Front side */
  .card--front { background: var(--paper); }
  .front-wave { position: absolute; inset: 0; width: 900px; height: 514px; }
  .card--front .wordmark {
    position: absolute;
    left: 62px;
    top: 70px;
    color: var(--ink);
    font-size: 34px;
  }
  .identity { position: absolute; left: 56px; top: 380px; }
  .identity__name { color: var(--amber); font-weight: 700; font-size: 27px; }
  .identity__title { color: var(--muted); font-weight: 300; font-size: 16px; margin-top: 6px; }
  .contact {
    position: absolute;
    left: 430px;
    top: 372px;
    list-style: none;
    color: var(--paper);
    font-weight: 300;
    font-size: 16px;
    line-height: 22px;
  }
  .contact li { display: flex; align-items: center; gap: 8px; }
  .contact svg { width: 13px; height: 13px; flex: none; }
  .contact__address { padding-left: 21px; }
</style>
</head>
<body>
  <section class="card card--back" aria-label="Card back">
    <span class="wordmark">Brisk Otter</span>
  </section>

  <section class="card card--front" aria-label="Card front">
    <svg class="front-wave" viewBox="0 0 900 514" aria-hidden="true">
      <path fill="var(--amber)" d="M0,172 C140,298 320,322 470,325 C660,328 800,268 900,236 L900,292 C800,312 660,334 470,336 C320,336 140,318 0,204 Z"/>
      <path fill="var(--ink)" d="M0,214 C140,330 320,346 470,346 C660,346 800,322 900,302 L900,514 L0,514 Z"/>
    </svg>

    <span class="wordmark">Brisk Otter</span>

    <div class="identity">
      <p class="identity__name">Dale Pemberton</p>
      <p class="identity__title">Director &amp; CEO</p>
    </div>

    <ul class="contact">
      <li>
        <svg viewBox="0 0 24 24"><path fill="var(--amber)" d="M6.6 10.8a15.1 15.1 0 0 0 6.6 6.6l2.2-2.2a1 1 0 0 1 1-.25 11.4 11.4 0 0 0 3.6.57 1 1 0 0 1 1 1V20a1 1 0 0 1-1 1A17 17 0 0 1 3 4a1 1 0 0 1 1-1h3.5a1 1 0 0 1 1 1c0 1.25.2 2.45.57 3.6a1 1 0 0 1-.25 1z"/></svg>
        905-555-0147
      </li>
      <li>
        <svg viewBox="0 0 24 24"><path fill="var(--amber)" d="M2 5h20v14H2z M2 5l10 8 10-8" stroke="var(--ink)" stroke-width="1.5"/></svg>
        dale@briskotterrecruiting.com
      </li>
      <li>
        <svg viewBox="0 0 24 24"><circle cx="12" cy="12" r="10" fill="var(--amber)"/><path d="M2 12h20M12 2c3 3 3 17 0 20M12 2c-3 3-3 17 0 20" stroke="var(--ink)" stroke-width="1.5" fill="none"/></svg>
        www.briskotterrecruiting.com
      </li>
      <li class="contact__address">48 Harbourview Lane,</li>
      <li class="contact__address">Port Elden, ON L0K 2T5</li>
    </ul>
  </section>
</body>
</html>
```